Hintergrundbild für meinen Corvelo-Account
Zielgruppe
Ich arbeite im coolsten Softwarehaus der Welt: TPS Talvenor Prozesswerk Steuerungen AG (https://www.talvenor-werk.com/). Ich möchte für mein Corvelo-Profil ein schönes Hintergrundbild haben . Im Moment habe ich nur einen schnöden Screenshot unserer Software-Suite.
Aufgabenstellung
Das Hintergrundbild sollte gemäss Corvelo-Empfehlung 1584x396 (Breite x Höhe) haben und kleiner als 8MB sein
Es sollten unsere Farben verwendet werden (s. Anhang). Es kann irgend etwas abtraktes sein - ein Linien-Gewirr, Wellen, Kreise, es können auch Prozessketten oder Charts oder so was sein. Es wäre cool, wenn noch das Firmenlogo mit dabei ist, es kann auch alles ein wenig verschwommen/ blured sein. Ich habe kleider noch gar keine konkrete Vorstellung.
Falls du Stockfotos verwenden möchtest, dann hab ich nur zugriff auf Pixmorada...

```html
<!DOCTYPE html>
<html lang="de">
<head>
<meta charset="utf-8">
<title>Corvelo Profil-Hintergrund – TPS</title>
<link rel="stylesheet" href="https://fonts.googleapis.com/css2?family=Source+Sans+3:wght@400;600&family=Arimo:wght@400&display=swap">
<style>
  :root {
    --page: #ffffff;
    --ink: #1d1d1d;
    --muted: #5e5e5e;
    --link: #0a66c2;
    --button: #0a66c2;
    --divider: #e6e6e6;
    --banner-text: #ffffff;
    --neutral-dot: #9aa3ad;
    --crowd-dark: #2a2c33;
    --crowd-mid: #4a5566;
  }
  * { box-sizing: border-box; margin: 0; padding: 0; }
  html, body { width: 1200px; height: 848px; overflow: hidden; background: var(--page); }
  .canvas { position: relative; width: 1200px; height: 848px; font-family: "Source Sans 3", sans-serif; color: var(--ink); }

  .banner {
    position: absolute; left: 219px; width: 761px; height: 191px; overflow: hidden;
    background:
      radial-gradient(ellipse 40% 60% at 48% 70%, rgba(40,42,50,0.9), transparent 70%),
      linear-gradient(160deg, transparent 60%, rgba(26,163,181,0.85) 78%, rgba(245,165,22,0.85) 100%),
      linear-gradient(90deg, #3b6c78 0%, var(--crowd-mid) 12%, var(--crowd-dark) 45%, var(--crowd-mid) 70%, #2f8a97 100%);
  }
  .banner--profile { top: 67px; }
  .banner--preview { top: 546px; }

  .banner__name {
    position: absolute; right: 18px; top: 62px;
    font-family: "Source Sans 3", sans-serif; font-weight: 600; font-size: 58px; line-height: 1;
    color: var(--banner-text); white-space: nowrap;
  }

  .profile-card { position: absolute; left: 220px; top: 258px; width: 759px; height: 258px; border-bottom: 1px solid var(--divider); border-radius: 0 0 8px 8px; }

  .avatar {
    position: absolute; left: 245px; top: 188px; width: 120px; height: 120px; border-radius: 50%;
    border: 4px solid var(--page); box-shadow: 0 2px 6px rgba(0,0,0,0.25);
    background: radial-gradient(circle at 60% 40%, #c9733a, #6b4a24 60%, #2b2a22);
  }

  .more { position: absolute; left: 934px; top: 280px; display: flex; gap: 4px; }
  .more span { width: 4px; height: 4px; background: var(--ink); }

  .name { position: absolute; left: 244px; top: 329px; font-size: 24px; font-weight: 600; line-height: 1.2; }
  .headline { position: absolute; left: 244px; top: 364px; font-size: 16px; }
  .location { position: absolute; left: 244px; top: 387px; font-size: 16px; color: var(--muted); }
  .stats { position: absolute; left: 244px; top: 410px; font-size: 16px; color: var(--muted); }

  .company { position: absolute; left: 688px; top: 333px; display: flex; align-items: center; gap: 9px; font-size: 16px; font-weight: 400; color: var(--link); }
  .company__dot { width: 12px; height: 12px; border-radius: 50%; background: var(--neutral-dot); }

  .signin { position: absolute; left: 243px; top: 446px; width: 283px; height: 46px; border-radius: 23px; background: var(--button); color: #fff; font-size: 15.5px; font-weight: 600; display: flex; align-items: center; justify-content: center; }

  .size-note { position: absolute; left: 224px; top: 750px; font-family: "Arimo", sans-serif; font-size: 17px; color: var(--ink); }
</style>
</head>
<body>
<div class="canvas">
  <div class="banner banner--profile" role="img" aria-label="Gruppenfoto der Belegschaft von oben, winkend, mit Markenfarben Petrol und Orange am rechten Rand">
    <div class="banner__name">TPS</div>
  </div>

  <div class="profile-card"></div>
  <div class="avatar" role="img" aria-label="Profilfoto"></div>
  <div class="more"><span></span><span></span><span></span></div>

  <div class="name">Tobias Marxen</div>
  <div class="headline">Human</div>
  <div class="location">Rebwil, Aargau, Schweiz</div>
  <div class="stats">558 Follower:innen &nbsp;·&nbsp; 500+ Kontakte</div>

  <div class="company"><span class="company__dot"></span>TPS</div>

  <div class="signin">Anmelden, um das Profil zu sehen</div>

  <div class="banner banner--preview" role="img" aria-label="Gruppenfoto der Belegschaft von oben, winkend, mit Markenfarben Petrol und Orange am rechten Rand">
    <div class="banner__name">TPS</div>
  </div>

  <div class="size-note">1584 px x 396 px</div>
</div>
</body>
</html>
```